QM Studios needs and Interior Design Business card

I can do anything from Commercial to Residential and Free lance. Beginning to end in design selection process.
Need something to catch the eye of potential customers and vendors. From furniture to Tile and Cabinet selections. I can do it all.

Industry/Entity Type

Design Agency

Contact Information for Business Card

QM Studios- Design Consultanting Residential, Commerical
Maybe a cool detail background. Wall paper print that can have some texture

Font styles to use
Serif

Colors
709dcb
34a6d7
b868aa
e667a6
f59296
85acd3
ffffff
000000
5c5c5c

Requirements
Must have
• Square or Rectangular with Rounded edges
• Name
• Address
• Phone
• Email
Nice to have
• Some colored edges More simples not too busy
• Pattern detail in background.
Should not have
• Not too much color

```html
<!DOCTYPE html>
<html lang="en">
<head>
<meta charset="utf-8">
<title>QM Studios – Business Card</title>
<link rel="stylesheet" href="https://fonts.googleapis.com/css2?family=Open+Sans:wght@400;700;800&display=swap">
<style>
  :root {
    --sky: #2fa3d6;
    --sky-dark: #2893c3;
    --ink: #000000;
    --grey: #2b2b2b;
    --rule: #bcbcbc;
    --paper: #ffffff;
    --backdrop: #e9ebee;
  }
  * { box-sizing: border-box; margin: 0; padding: 0; }
  html, body { width: 1200px; height: 900px; overflow: hidden; }
  body {
    background: var(--backdrop);
    font-family: "Open Sans", sans-serif;
    position: relative;
  }
  .card {
    position: absolute;
    left: 320px;
    width: 560px;
    height: 320px;
    border-radius: 24px;
    overflow: hidden;
    box-shadow: 0 10px 30px rgba(0,0,0,.18);
  }
  .brand-name { white-space: nowrap; font-weight: 400; }
  .brand-dot { display: block; border-radius: 50%; flex: none; }

  /* Back */
  .card-back { top: 90px; background: var(--sky); }
  .card-back .pattern {
    position: absolute; inset: 0;
    background: linear-gradient(135deg, var(--sky) 0%, var(--sky-dark) 100%);
  }
  .back-brand {
    position: absolute;
    left: 50%; top: 50%;
    transform: translate(-50%, -50%);
    display: flex; align-items: center; gap: 22px;
  }
  .back-brand .brand-dot {
    width: 110px; height: 110px;
    border: 6px solid var(--paper);
  }
  .back-brand .brand-name {
    color: var(--paper);
    font-size: 38px;
    letter-spacing: 5px;
  }

  /* Front */
  .card-front { top: 480px; background: var(--paper); }
  .swoosh { position: absolute; left: 0; top: 0; width: 560px; height: 320px; }
  .front-brand {
    position: absolute;
    left: 30px; top: 46px;
    width: 250px;
    display: flex; flex-direction: column; align-items: center; gap: 12px;
  }
  .front-brand .brand-dot {
    width: 88px; height: 88px;
    border: 5px solid var(--ink);
  }
  .front-brand .brand-name {
    color: var(--ink);
    font-size: 30px;
    letter-spacing: 5px;
  }
  .divider {
    position: absolute;
    left: 298px; top: 36px;
    width: 1px; height: 130px;
    background: var(--rule);
  }
  .contact {
    position: absolute;
    left: 316px; top: 34px;
    color: var(--grey);
    font-size: 13px;
    line-height: 1.35;
  }
  .contact .person { color: var(--ink); font-size: 21px; font-weight: 800; line-height: 1.1; }
  .contact .role { color: var(--sky); font-size: 12px; letter-spacing: .5px; margin-bottom: 6px; }
  .contact .address { margin-bottom: 8px; }
  .contact .line { display: flex; align-items: center; gap: 6px; }
  .contact .line svg { width: 10px; height: 10px; fill: var(--sky); }
</style>
</head>
<body>
  <section class="card card-back">
    <div class="pattern" role="img" aria-label="Faint repeating wallpaper pattern in blue tones"></div>
    <div class="back-brand">
      <span class="brand-dot"></span>
      <span class="brand-name">QM Studios</span>
    </div>
  </section>

  <section class="card card-front">
    <svg class="swoosh" viewBox="0 0 560 320" aria-hidden="true">
      <path d="M0 276 C 250 268, 450 240, 560 186 L560 320 L0 320 Z" fill="var(--sky)"/>
      <path d="M0 262 C 250 254, 450 226, 560 174 L560 182 C 450 236, 250 264, 0 272 Z" fill="var(--ink)"/>
    </svg>
    <div class="front-brand">
      <span class="brand-dot"></span>
      <span class="brand-name">QM Studios</span>
    </div>
    <div class="divider"></div>
    <div class="contact">
      <p class="person">MARA QUINLAN</p>
      <p class="role">DIRECTOR</p>
      <p class="address">Unit 2/8 Harlow Lane<br>KELVIN, QLD 4120</p>
      <p class="line"><svg viewBox="0 0 10 10"><path d="M2 0.5 L3.8 2.6 L2.8 3.6 Q4 5.8 6.4 7.2 L7.4 6.2 L9.5 8 L8 9.5 Q3.5 9 0.5 2 Z"/></svg>+330 5187-2036</p>
      <p class="line"><svg viewBox="0 0 10 10"><path d="M0 2 H10 V8 H0 Z M0.8 2.6 L5 5.6 L9.2 2.6 V3.4 L5 6.4 L0.8 3.4 Z" fill-rule="evenodd"/></svg>info@qmstudios.com</p>
    </div>
  </section>
</body>
</html>
```